New Wine Label - Classy, Simple, Modern

We are a small boutique winery who have been making and selling wine for 21 years. We are called "Velmoran Winery" and Velmoran is the Greek God of wine. We have a classic label at the moment that we would like to modernise.

We are looking to update our labels while keeping some of the original elements.
From existing label to definitely keep:
1. Logo (Colour can be darkened to a very dark purple - almost black)
2. Legal requirements - Front Label: 750ml, variety, year, "Canberra District" Back Label: Produce of Australia, number of standard drinks, alc/vol, additives, internet address, bar code plus new requirement to warn pregnant women alcohol can harm their babies.
From existing label open to change:
3. What would be nice - Separate front and back labels. Focus on logo on front label (Possibly printed in a raised gloss/embossed), Modern Font,
4. What can we lose? Happy to lose the words about us.
5.Font - Modern, Colour - white background, Shape Rectangular Front approximately height 11cm width 9cm & Back height 9cm width 7cm.

Prototype label can be for a
Front:
2022 Cabernet Sauvignon, Canberra District, 750ml, Estate Grown and Made
Back
13.6%ALC/VOL, APPROX 8.0 STANDARD DRINKS, PRESERVATIVE (220) ADDED, PRODUCE OF AUSTRALIA, Bar Code, Pregnant women warning, www.velmoran-winery.com.au

if you want to use some words to describe the wine that's fine - you can make some up or use existing words from our website www.velmoran-winery.com.au

Files:
1 - Photo of existing front label
2 - Current printers spec sheet for front and back label
3 - Pregnancy warning graphic (specific details see link below - label type 1)
4 - Current Bar Code for Cabernet Sauvignon
Many file types of existing logo

Link to legal requirement for pregnant women warning - we need label type 1 -https://www.trelvacorp.gov.au/sector/packaging/Pages/caution-notice-labels-downloadable-files.aspx

25 - 40 year olds, drink wine

Winery - Wine Production

```html
<!DOCTYPE html>
<html lang="en">
<head>
<meta charset="utf-8">
<title>Velmoran Winery – Cabernet Sauvignon Back Label</title>
<link rel="stylesheet" href="https://fonts.googleapis.com/css2?family=Josefin+Sans:wght@300;400;600;700&display=swap">
<style>
  :root {
    --ink: #111111;
    --gold: #b8934f;
    --paper: #ffffff;
    --stage: #f1f0ee;
    --band: #0d0d0d;
    --band-text: #ffffff;
    --rule: #e2e0dc;
  }
  * { box-sizing: border-box; margin: 0; padding: 0; }
  html, body {
    width: 1200px;
    height: 1200px;
    overflow: hidden;
    background: var(--stage);
  }
  .canvas {
    position: relative;
    width: 1200px;
    height: 1200px;
  }
  .back-label {
    position: absolute;
    left: 180px;
    top: 60px;
    width: 840px;
    height: 1080px;
    background: var(--paper);
    border: 1px solid var(--rule);
    font-family: "Josefin Sans", sans-serif;
    color: var(--ink);
    text-align: center;
  }
  .brand-name {
    position: absolute;
    top: 48px;
    left: 0;
    right: 0;
    font-weight: 600;
    color: var(--ink);
    line-height: 1;
  }
  .brand-name__main {
    display: block;
    font-size: 66px;
    letter-spacing: 10px;
    padding-left: 10px;
  }
  .brand-name__sub {
    display: block;
    margin-top: 14px;
    font-size: 46px;
    letter-spacing: 5px;
    padding-left: 5px;
  }
  .variety {
    position: absolute;
    top: 200px;
    left: 0;
    right: 0;
    font-size: 41px;
    font-weight: 400;
    letter-spacing: 6px;
    color: var(--gold);
  }
  .tasting-note {
    position: absolute;
    top: 274px;
    left: 74px;
    right: 74px;
    font-size: 27px;
    font-weight: 300;
    letter-spacing: 2px;
    text-transform: uppercase;
  }
  .tasting-note__line {
    display: block;
    height: 40px;
    line-height: 40px;
    text-align: justify;
    text-align-last: justify;
  }
  .tasting-note__line--last {
    text-align-last: center;
  }
  .legal {
    position: absolute;
    top: 498px;
    left: 0;
    right: 0;
    font-size: 19px;
    font-weight: 600;
    letter-spacing: 2px;
    line-height: 34px;
  }
  .volume {
    position: absolute;
    top: 596px;
    left: 0;
    right: 0;
    font-size: 52px;
    font-weight: 700;
    letter-spacing: 6px;
    color: var(--gold);
  }
  .abv {
    position: absolute;
    top: 662px;
    left: 0;
    right: 0;
    font-size: 25px;
    font-weight: 600;
    letter-spacing: 3px;
    color: var(--gold);
  }
  .symbols {
    position: absolute;
    top: 700px;
    left: 0;
    right: 0;
    display: flex;
    justify-content: center;
    gap: 26px;
  }
  .symbols svg { width: 68px; height: 68px; }
  .footer-band {
    position: absolute;
    left: 0;
    right: 0;
    bottom: 0;
    height: 114px;
    background: var(--band);
    border-top: 5px solid var(--gold);
    border-bottom: 4px solid var(--gold);
    padding-top: 22px;
  }
  .origin {
    font-size: 25px;
    font-weight: 400;
    letter-spacing: 3px;
    color: var(--band-text);
  }
  .web-address {
    margin-top: 12px;
    font-size: 27px;
    font-weight: 600;
    letter-spacing: 3.5px;
    color: var(--gold);
  }
</style>
</head>
<body>
<main class="canvas">
  <section class="back-label">
    <h1 class="brand-name">
      <span class="brand-name__main">VELMORAN</span>
      <span class="brand-name__sub">WINERY</span>
    </h1>

    <h2 class="variety">CABERNET SAUVIGNON</h2>

    <p class="tasting-note">
      <span class="tasting-note__line">A wine full of promise with a deep</span>
      <span class="tasting-note__line">colour, and firm structure backed up</span>
      <span class="tasting-note__line">with rich fruit and herbal aromas. The</span>
      <span class="tasting-note__line">long, luscious palate has great fruit</span>
      <span class="tasting-note__line tasting-note__line--last">intensity and depth of flavour.</span>
    </p>

    <p class="legal">APPROX 8.0 STANDARD DRINKS<br>PRESERVATIVE (220) ADDED</p>

    <p class="volume">750 ML</p>
    <p class="abv">13.6%ALC/VOL</p>

    <div class="symbols">
      <svg role="img" aria-label="Pregnancy warning symbol" viewBox="0 0 68 68">
        <circle cx="34" cy="34" r="32" fill="var(--gold)"/>
      </svg>
      <svg role="img" aria-label="Recycling symbol" viewBox="0 0 68 68">
        <rect x="4" y="4" width="60" height="60" rx="6" fill="var(--gold)"/>
      </svg>
    </div>

    <footer class="footer-band">
      <p class="origin">PRODUCE OF AUSTRALIA</p>
      <p class="web-address">www.velmoran-winery.com.au</p>
    </footer>
  </section>
</main>
</body>
</html>
```